Website redesign for a Medical Office

We are a physician office in need of a website redesign and a face-lift.
1.Website must work on all platforms including mobile phones and tablets.
2.Website will also include and interactive CONTACT US form and payment gateway for office to collect payment from patients online.
3.Website should have the ability for us to easily edit content without resorting to the services of an IT person.
4. Website content will be collected from the present website www.bramblewoodkids.com.
- The type of upgrade we are looking for is more of a corrective work. The major problems with the current website are:
1. Contact Us form not working correctly
2. Credit card/zentro gateway not working as intended
3. Needing better images/pictures to correctly reflect our business.
4. General enhancement to the overall feel and outlook of the current website.

5. Once a design is selected, website MUST be up and live within TWO WEEKS. The designer able to make this work within the time-frame will get an extra bonus.

Target Market(s)

General public; including patients and their parents.

Industry/Entity Type

Healthcare

Coding

Coded - Design and coding required

Number of Pages Required

5+ page

Font styles to use
Sans Serif

Colors
0492cd
33a6d7
85cae6
cee9f5
cedeed
acd036
cadf82
00a990
f04a50

Requirements
Must have
• 1. Ability for the website to work on all platforms including mobile phones and tablets.
• 2. Include an interactive CONTACT US form
• 3. A payment gateway for office to collect payment from patients online using credit cards and Zentro.
• 4. Website should have the ability for us to easily edit content without resorting to the services of an IT person.
• 5. Once a design is selected, website MUST be up and live within TWO WEEKS.
• 6. Social network buttons.
• 7. A Lorvex map with office location or geo-tag and directions to office.
Nice to have
• Nice theme, children friendly with a flashy home page and inside pages.
• Attractive design with wow factor

```html
<!DOCTYPE html>
<html lang="en">
<head>
<meta charset="utf-8">
<title>Bramblewood Kids</title>
<link href="https://fonts.googleapis.com/css2?family=Roboto:wght@300;400;500;700&display=swap" rel="stylesheet">
<style>
:root{
  --teal:#22c39c;
  --teal-dark:#1aa986;
  --orange:#ff8b5e;
  --yellow:#f5d24b;
  --red:#f04a50;
  --blue:#0492cd;
  --navy:#1f5aa0;
  --brand:#2b3fbf;
  --text:#555;
  --muted:#888;
  --light:#eef6fb;
  --footer:#1c6650;
  --white:#fff;
}
*{box-sizing:border-box;margin:0;padding:0}
html,body{width:1200px;height:3523px;overflow:hidden}
body{font-family:"Roboto",sans-serif;color:var(--text);background:var(--white);position:relative}
section,header,footer,nav{position:relative;width:1200px}
.abs{position:absolute}
a{color:inherit;text-decoration:none}

/* top bar */
.topbar{height:28px;font-size:12px;color:#666}
.topbar .social{left:80px;top:8px;display:flex;gap:8px}
.topbar .social span{width:11px;height:11px;background:var(--blue);border-radius:2px;display:block}
.topbar .info{right:80px;top:7px;display:flex;gap:28px}
.topbar .info i{display:inline-block;width:10px;height:10px;border-radius:50%;background:var(--teal);margin-right:6px;vertical-align:-1px}

/* nav */
.nav{height:89px}
.brand{left:80px;top:24px;display:flex;align-items:center;gap:10px;font-weight:700;font-size:22px;color:var(--brand);letter-spacing:.5px}
.brand b{width:36px;height:36px;background:var(--brand);display:block}
.menu{right:80px;top:30px;display:flex;align-items:center;gap:24px;font-size:15px;color:#333}
.menu .cta{background:var(--teal);color:var(--white);padding:10px 22px}

/* hero */
.hero{height:517px;background:linear-gradient(100deg,#d9d3cc 0%,#efe9e2 45%,#e6dfd6 100%)}
.appt{left:751px;top:64px;width:331px;height:406px;background:var(--white);box-shadow:0 2px 10px rgba(0,0,0,.15)}
.appt h3{background:var(--red);color:var(--white);font-size:17px;font-weight:500;padding:10px 18px;margin:-5px -12px 0 0;width:343px}
.appt .field{margin:8px 28px 0;background:#ececec;height:36px;font-size:10px;color:#888;padding:11px 12px;text-transform:uppercase}
.appt .field.tall{height:66px}
.appt .field.date{height:50px;line-height:16px;padding-top:8px}
.appt .btn{margin:18px 28px 0;background:var(--teal);color:var(--white);text-align:center;font-size:17px;padding:9px 0}

/* feature boxes */
.features{height:211px;display:flex}
.feature{width:400px;height:211px;padding:30px 40px;color:var(--white)}
.feature small{font-size:12px;display:block}
.feature h4{font-size:20px;font-weight:700;margin:4px 0 14px;text-transform:uppercase}
.feature p{font-size:12px;line-height:17px;opacity:.85}
.feature a{display:block;margin-top:14px;font-size:12px;font-weight:700}
.f1{background:var(--teal)}.f2{background:var(--orange)}.f3{background:var(--yellow)}

/* headings */
.title{text-align:center;font-weight:400;font-size:38px;line-height:45px;color:#333}
.divider{display:block;margin:8px auto 0;width:22px;height:14px;border:2px solid #ccc;border-radius:4px}
.lead{font-size:13px;line-height:22px;text-align:center;color:#666;width:900px;margin:0 auto}

/* specialize */
.special{height:599px;padding-top:62px}
.special .lead{margin-top:20px}
.cards{left:80px;top:240px;display:flex;gap:14px}
.card{width:249px;height:300px;border:1px solid #ddd;background:var(--white);text-align:center}
.card .photo{height:140px;display:block}
.card h5{font-size:17px;font-weight:500;margin:18px 0 8px}
.card p{font-size:12.5px;line-height:17px;color:#888;padding:0 16px}
.card .bar{display:block;width:74px;height:4px;margin:10px auto 0}
.c1 h5,.c3 h5{color:var(--teal)} .c1 .bar,.c3 .bar{background:var(--teal)}
.c2 h5{color:var(--orange)} .c2 .bar{background:var(--orange)}
.c4 h5{color:var(--yellow)} .c4 .bar{background:var(--yellow)}

/* about */
.about{height:523px}
.about svg.band{left:0;top:0}
.about h2{left:80px;top:112px;color:var(--white);font-size:38px;font-weight:400}
.about .mark{left:80px;top:166px;width:22px;height:18px;background:var(--brand)}
.about .copy{left:80px;top:206px;width:440px;color:var(--white);font-size:13px;line-height:22px}
.about .copy p+p{margin-top:14px}
.about .photo{left:578px;top:117px;width:556px;height:287px}

/* health center */
.health{height:663px;padding-top:52px}
.health .lead{margin-top:6px}
.topics{left:80px;top:258px;width:380px}
.topics li{list-style:none;font-size:17px;line-height:20px;font-weight:700;position:relative;padding-left:30px;margin-bottom:18px}
.topics li::before{content:"";position:absolute;left:0;top:3px;width:14px;height:14px;border:1px solid #ccc;border-radius:50%}
.topics .t1{color:var(--teal)}
.topics .t2{color:var(--yellow)}
.topics .t2::before{border-radius:0;background:var(--yellow);border-color:var(--yellow)}
.topics .sub{margin:8px 0 0;font-weight:400;font-size:13.5px;color:#555;line-height:19px}
.topics .t3{color:var(--red)}
.topics .t4{color:#2a2a7a}
.topics .t5{color:var(--blue)}
.topics .t6{color:var(--orange)}
.gallery{left:481px;top:254px;width:639px;height:348px;display:grid;grid-template-columns:200px 229px 200px;grid-template-rows:171px 171px;gap:6px}
.gallery span{display:block}
.g1{grid-row:1/3}.g4{grid-row:1/3;grid-column:3}

/* stats band */
.stats{height:188px;background:var(--navy)}
.stats h3{left:80px;top:28px;width:520px;color:var(--white);font-size:26px;font-weight:500;line-height:38px}
.stats .btn{left:80px;top:128px;background:var(--teal);color:var(--white);font-size:14px;padding:11px 28px}
.stats .sep{left:602px;top:38px;width:1px;height:100px;background:rgba(255,255,255,.5)}
.stat{top:34px;width:140px;text-align:center;color:var(--white);font-size:14px}
.stat svg{display:block;margin:0 auto 12px}

/* testimonials */
.reviews{height:394px;background:var(--light);padding-top:42px}
.reviews .quote{top:120px;font-size:120px;line-height:100px;color:var(--navy);font-family:"Roboto",sans-serif;font-weight:700}
.reviews .text{left:168px;top:124px;width:870px;font-size:13.5px;line-height:22px;color:#555}
.reviews .track{left:158px;top:222px;width:476px;height:1px;background:#bbb}
.reviews .knob{left:154px;top:216px;width:14px;height:14px;background:var(--navy)}
.people{left:170px;top:286px;display:flex;gap:0}
.person{width:270px;display:flex;align-items:center;gap:14px;font-size:14px}
.person span{width:60px;height:60px;border-radius:50%;display:block;background:#ddd}
.person.on span{background:#d8b488;box-shadow:0 0 0 3px #fff,0 0 0 4px #ccc}
.person.on{color:var(--navy)}
.person.off{color:#bbb}

/* footer */
.footer{height:311px;background:var(--footer);color:var(--white)}
.footer .brand{left:80px;top:48px;color:var(--white);font-size:20px}
.footer .brand b{background:var(--white)}
.footer .about-text{left:80px;top:134px;width:230px;font-size:12.5px;line-height:18px}
.footer h6{font-size:13px;font-weight:500}
.links{left:352px;top:48px}
.links ul{list-style:none;margin-top:22px;font-size:12px;line-height:21.5px}
.contact{left:568px;top:48px}
.contact dl{margin-top:32px;display:grid;grid-template-columns:90px 190px;row-gap:14px;font-size:12px;line-height:17px}
.map{left:910px;top:80px;width:210px;height:130px;background:linear-gradient(135deg,#e8e4da,#d7dfe4)}
.footer .rule{left:80px;top:276px;width:1040px;height:1px;background:rgba(255,255,255,.25)}
.footer .copy{left:80px;top:286px;font-size:11px}
.footer .fsocial{right:80px;top:286px;display:flex;gap:24px}
.footer .fsocial span{width:11px;height:11px;background:var(--white);display:block;border-radius:2px}
</style>
</head>
<body>

<header class="topbar">
  <div class="abs social"><span></span><span></span><span></span><span></span></div>
  <div class="abs info"><span><i></i>Opening Hours : M-F 8:30AM - 5:30PM</span><span><i></i>Emergency Line : (555) 014-2290</span></div>
</header>

<nav class="nav">
  <div class="abs brand"><b></b>Bramblewood Kids</div>
  <div class="abs menu"><a>HOME</a><a>ABOUT US</a><a>SERVICES</a><a>PRIME HEALTH CENTER</a><a>FORM</a><a>NEWS</a><a class="cta">CONTACT</a></div>
</nav>

<section class="hero">
  <div class="abs" style="left:0;top:0;width:720px;height:517px;background:linear-gradient(90deg,#cfc8c0,#e4ddd4 60%,#d7cfc5)" role="img" aria-label="Doctor examining a young boy with a stethoscope"></div>
  <form class="abs appt">
    <h3>Request an Appointment</h3>
    <div class="field" style="margin-top:18px">Your Name</div>
    <div class="field">Email Address</div>
    <div class="field">Phone Number</div>
    <div class="field date">Booking Date<br>◷ 01-03-2017</div>
    <div class="field tall">Massage</div>
    <div class="btn">BOOK NOW</div>
  </form>
</section>

<section class="features">
  <div class="feature f1"><small>Quick Help</small><h4>Emergency Cases</h4><p>Sed ut perspiciatis unde omnis iste natus error sit voluptatem accusantium doloremque veritatis et quasi explicabo.</p><a>Read More</a></div>
  <div class="feature f2"><small>In Our Country</small><h4>5 Branches</h4><p>Sed ut perspiciatis unde omnis iste natus error sit voluptatem accusantium doloremque veritatis et quasi explicabo.</p><a>Read More</a></div>
  <div class="feature f3"><small>Smooth and Easy</small><h4>Online Bill Payments</h4><p>Sed ut perspiciatis unde omnis iste natus error sit voluptatem accusantium doloremque veritatis et quasi explicabo.</p><a>Read More</a></div>
</section>

<section class="special">
  <h2 class="title">We Specialize In</h2><span class="divider"></span>
  <p class="lead">Bramblewood Kids is a modern pediatric practice dedicated to the health and wellness of children. It is the pediatrician office of choice in Fairhollow, Georgia. At Bramblewood Kids, you will find a pediatrician and an environment that is warm and compassionate. All of our staff members are knowledgeable, caring, efficient, and ready to serve you.</p>
  <div class="abs cards">
    <div class="card c1"><span class="photo" role="img" aria-label="Doctor consulting a mother and child" style="background:linear-gradient(135deg,#dfe8ee,#b9cfdc)"></span><h5>General Medical Care</h5><p>Routine Office visits for common ailment, Immunizations, ADHD Evaluation and Treatment, Asthma Care, Allergy Testing, Same day SICK appointments</p><span class="bar"></span></div>
    <div class="card c2"><span class="photo" role="img" aria-label="Mother holding a newborn baby" style="background:linear-gradient(135deg,#f2dcc8,#d9b79a)"></span><h5>Newborn Care</h5><p>Routine Office visits for common ailment, Immunizations, ADHD Evaluation and Treatment, Asthma Care, Allergy Testing, Same day SICK appointments</p><span class="bar"></span></div>
    <div class="card c3"><span class="photo" role="img" aria-label="Physical examination with x-ray screen" style="background:linear-gradient(135deg,#c9ccd2,#8a939f)"></span><h5>Physical Examinations</h5><p>Routine Office visits for common ailment, Immunizations, ADHD Evaluation and Treatment, Asthma Care, Allergy Testing, Same day SICK appointments</p><span class="bar"></span></div>
    <div class="card c4"><span class="photo" role="img" aria-label="Emergency staff in a hospital corridor" style="background:linear-gradient(135deg,#c7b9a3,#8e7c66)"></span><h5>Emergency Care</h5><p>Routine Office visits for common ailment, Immunizations, ADHD Evaluation and Treatment, Asthma Care, Allergy Testing, Same day SICK appointments</p><span class="bar"></span></div>
  </div>
</section>

<section class="about">
  <svg class="abs band" width="1200" height="523" viewBox="0 0 1200 523"><polygon points="0,0 600,36 1200,0 1200,523 600,480 0,523" fill="var(--teal)"/></svg>
  <h2 class="abs">About US</h2>
  <span class="abs mark"></span>
  <div class="abs copy">
    <p>Bramblewood Kids is a modern pediatric practice dedicated to the health and wellness of children. It is the pediatrician office of choice in Fairhollow, Georgia.</p>
    <p>At Bramblewood Kids, you will find a pediatrician and an environment that is warm and compassionate. All of our staff members are knowledgeable, caring, efficient, and ready to serve you. The general atmosphere is pleasant, flexible and fun-filled for you and your family to enjoy. It is our pleasure to provide you and your children with our wide range of services.</p>
  </div>
  <div class="abs photo" role="img" aria-label="Two children playing doctor with a toy stethoscope" style="background:linear-gradient(120deg,#e9a7a0,#f1e4d6 50%,#b9d3ea)"></div>
</section>

<section class="health">
  <h2 class="title">PRIME HEALTH CENTER</h2><span class="divider"></span>
  <p class="lead">Bramblewood Kids is a modern pediatric practice dedicated to the health and wellness of children. It is the pediatrician office of choice in Fairhollow, Georgia. At Bramblewood Kids, you will find a pediatrician and an environment that is warm and compassionate. All of our staff members are knowledgeable, caring, efficient, and ready to serve you.</p>
  <ul class="abs topics">
    <li class="t1">Well Child Information</li>
    <li class="t2">Immunizations
      <div class="sub">Vaccine Policy<br>Recommended Immunization Schedule<br>Catch-up Schedule<br>Vaccines and Disease Prevention<br>Images of Some Vaccine Preventable Diseases<br>Videos of Some Vaccine Preventable Diseases</div></li>
    <li class="t3">Newborn Care</li>
    <li class="t4">Now That You Are Pregnant</li>
    <li class="t5">Parenting Resources</li>
    <li class="t6">Common Childhood Illnesses</li>
  </ul>
  <div class="abs gallery">
    <span class="g1" role="img" aria-label="Mother comforting her child" style="background:linear-gradient(160deg,#d8c3b0,#a98d78)"></span>
    <span class="g2" role="img" aria-label="Doctor checking a toddler" style="background:linear-gradient(160deg,#f1ede8,#c7b9ab)"></span>
    <span class="g4" role="img" aria-label="Mother holding a newborn" style="background:linear-gradient(160deg,#f0d9c6,#cfa586)"></span>
    <span class="g3" role="img" aria-label="Child at a checkup with a doctor" style="background:linear-gradient(160deg,#e7eef4,#a5b6c6)"></span>
  </div>
</section>

<section class="stats">
  <h3 class="abs">We Are Served Since 8 Years To Our Customer With Trust And We are</h3>
  <a class="abs btn">BOOK AN APPOINTMENT</a>
  <span class="abs sep"></span>
  <div class="abs stat" style="left:624px">
    <svg width="62" height="62" viewBox="0 0 62 62"><circle cx="31" cy="31" r="29" fill="#fff"/><circle cx="31" cy="23" r="8" fill="var(--navy)"/><path d="M16 48c2-10 8-14 15-14s13 4 15 14z" fill="var(--navy)"/></svg>Total Doctor</div>
  <div class="abs stat" style="left:800px">
    <svg width="62" height="62" viewBox="0 0 62 62"><circle cx="31" cy="31" r="29" fill="#fff"/><path d="M24 14v14a7 7 0 0 0 14 0V14M31 35v8a6 6 0 0 0 12 0v-4" stroke="var(--navy)" stroke-width="3" fill="none"/><circle cx="43" cy="37" r="3" fill="var(--navy)"/></svg>Happy patient</div>
  <div class="abs stat" style="left:970px">
    <svg width="62" height="62" viewBox="0 0 62 62"><circle cx="31" cy="31" r="29" fill="#fff"/><path d="M15 20v24M15 36h32v8M15 30h32v6" stroke="var(--navy)" stroke-width="3" fill="none"/><circle cx="22" cy="30" r="3" fill="var(--navy)"/></svg>Total Bed</div>
</section>

<section class="reviews">
  <h2 class="title">WHAT PEOPLE SAYS</h2><span class="divider"></span>
  <div class="abs quote" style="left:80px">“</div>
  <div class="abs quote" style="left:1048px">”</div>
  <p class="abs text">Nemo enim ipsam voluptatem quia voluptas sit aspernatur aut odit aut fugit, sed quia consequuntur magni dolores eos qui ratione voluptatem sequi nesciunt. Neque porro quisquam est, qui dolorem ipsum quia dolor sit amet, consectetur, adipisci velit, sed quia non numquam eius modi tempora incidunt ut labore et dolore magnam aliquam quaerat voluptatem.</p>
  <span class="abs track"></span><span class="abs knob"></span>
  <div class="abs people">
    <div class="person on"><span role="img" aria-label="Portrait of Tessa"></span>Tessa</div>
    <div class="person off"><span role="img" aria-label="Portrait of Orin"></span>Orin</div>
    <div class="person off"><span role="img" aria-label="Portrait of Dalby"></span>Dalby</div>
    <div class="person off"><span role="img" aria-label="Portrait of Wrenna"></span>Wrenna</div>
  </div>
</section>

<footer class="footer">
  <div class="abs brand"><b></b>Bramblewood Kids</div>
  <p class="abs about-text">Sed ut perspiciatis unde omnis iste natus error sit accusantium doloremque totam rem aperiam.</p>
  <div class="abs links"><h6>QUICK LINK</h6>
    <ul><li>Home</li><li>About Us</li><li>Services</li><li>Prime Health Center</li><li>Form</li><li>News</li><li>Contact</li></ul></div>
  <div class="abs contact"><h6>CONTACT US</h6>
    <dl><dt>Address:</dt><dd>Bramblewood Kids 42 Larkspur Lane, Fairhollow, GA 30000</dd><dt>Mobile No:</dt><dd>(555) 014-2290</dd><dt>Email:</dt><dd>www.bramblewoodkids.com</dd></dl></div>
  <div class="abs map" role="img" aria-label="Street map showing the office location"></div>
  <span class="abs rule"></span>
  <p class="abs copy">COPYRIGHT © 2017 ALL RIGHT RESERVED</p>
  <div class="abs fsocial"><span></span><span></span><span></span><span></span></div>
</footer>

</body>
</html>
```